Create a professional, eye-catching business card design that reflects the values and services of Brookfern Veterinary Hospital. we provide veterinary services and the business card should be a memorable representation of the clinic and align with its branding and mission. our tag line is "Life Long Companions, Lifelong Care"
Use clean, modern typography. Prioritize readability and professionalism. We would like to see designs that use the color blue, as in the logo example. the final design should communicate professionalism and care, with attention to detail.

```html
<!DOCTYPE html>
<html lang="en">
<head>
<meta charset="utf-8">
<title>Brookfern Veterinary Hospital – Business Card</title>
<link href="https://fonts.googleapis.com/css2?family=Montserrat:wght@400;500;700;800&display=swap" rel="stylesheet">
<style>
  :root {
    --navy: #1d3360;
    --white: #ffffff;
    --ink: #1f1f24;
    --backdrop: #8a8a8a;
    --facet-light: #f6f6f7;
    --facet-mid: #ebebee;
  }
  * { margin: 0; padding: 0; box-sizing: border-box; }
  html, body {
    width: 1200px; height: 1200px; overflow: hidden;
    background: var(--backdrop);
    font-family: "Montserrat", Arial, sans-serif;
  }
  .canvas { position: relative; width: 1200px; height: 1200px; }

  .card { position: absolute; left: 156px; width: 885px; height: 516px; background: var(--white); overflow: hidden; }
  .card-front { top: 60px; }
  .card-back { top: 621px; }

  .brand-panel { position: absolute; left: 0; top: 0; width: 433px; height: 100%; background: var(--navy); }
  .facet-texture {
    position: absolute; left: 433px; top: 0; right: 0; bottom: 0;
    background: linear-gradient(135deg, var(--facet-mid) 0%, var(--white) 35%, var(--facet-light) 60%, var(--white) 80%, var(--facet-mid) 100%);
  }

  .brand-mark { position: absolute; text-align: center; font-weight: 800; }
  .brand-mark .ring { display: block; margin: 0 auto; }
  .brand-name { display: block; line-height: 1; letter-spacing: 0.5px; }
  .brand-sub { display: block; line-height: 1; letter-spacing: 0.6px; }

  .brand-mark.on-navy { left: 0; top: 150px; width: 433px; color: var(--white); }
  .on-navy .brand-name { font-size: 46px; margin-top: 24px; }
  .on-navy .brand-sub { font-size: 17px; margin-top: 6px; }

  .brand-mark.on-white { left: 0; top: 150px; width: 885px; color: var(--navy); }
  .on-white .brand-name { font-size: 72px; margin-top: 24px; }
  .on-white .brand-sub { font-size: 25px; margin-top: 6px; }

  .contact-list { position: absolute; left: 495px; top: 155px; list-style: none; color: var(--ink); font-size: 21px; font-weight: 500; }
  .contact-item { display: flex; align-items: flex-start; margin-bottom: 14px; line-height: 1.4; }
  .contact-item.address { margin-top: 38px; }
  .contact-item.web { color: var(--navy); font-weight: 700; }
  .contact-icon { width: 20px; height: 20px; margin-right: 20px; margin-top: 4px; flex: none; fill: var(--navy); }
</style>
</head>
<body>
<main class="canvas">

  <section class="card card-front">
    <div class="brand-panel">
      <div class="brand-mark on-navy">
        <svg class="ring" width="130" height="130" viewBox="0 0 130 130" aria-hidden="true">
          <circle cx="65" cy="65" r="60" fill="none" stroke="var(--white)" stroke-width="3"/>
        </svg>
        <span class="brand-name">BROOKFERN</span>
        <span class="brand-sub">VETERINARY HOSPITAL</span>
      </div>
    </div>
    <div class="facet-texture" role="img" aria-label="Soft light grey faceted geometric background texture"></div>

    <ul class="contact-list">
      <li class="contact-item">
        <svg class="contact-icon" viewBox="0 0 24 24" aria-hidden="true"><path d="M6.6 10.8a15.1 15.1 0 0 0 6.6 6.6l2.2-2.2a1 1 0 0 1 1-.25 11.4 11.4 0 0 0 3.6.57 1 1 0 0 1 1 1V20a1 1 0 0 1-1 1A17 17 0 0 1 3 4a1 1 0 0 1 1-1h3.5a1 1 0 0 1 1 1c0 1.25.2 2.45.57 3.57a1 1 0 0 1-.25 1z"/></svg>
        <span>0161 482 739</span>
      </li>
      <li class="contact-item">
        <svg class="contact-icon" viewBox="0 0 24 24" aria-hidden="true"><path d="M3 5h18v14H3z M3 6l9 6 9-6v2l-9 6-9-6z" fill-rule="evenodd"/></svg>
        <span>hello@brookfernvet.com</span>
      </li>
      <li class="contact-item web">
        <svg class="contact-icon" viewBox="0 0 24 24" aria-hidden="true"><path d="M12 2a10 10 0 1 0 0 20 10 10 0 0 0 0-20zm6.9 6h-3a15.6 15.6 0 0 0-1.4-3.6A8 8 0 0 1 18.9 8zM12 4c.8 1.2 1.5 2.5 1.9 4h-3.8c.4-1.5 1.1-2.8 1.9-4zM4.3 14a8 8 0 0 1 0-4h3.4a16 16 0 0 0 0 4zm.8 2h3a15.6 15.6 0 0 0 1.4 3.6A8 8 0 0 1 5.1 16zm3-8h-3a8 8 0 0 1 4.4-3.6A15.6 15.6 0 0 0 8.1 8zM12 20c-.8-1.2-1.5-2.5-1.9-4h3.8c-.4 1.5-1.1 2.8-1.9 4zm2.3-6H9.7a14 14 0 0 1 0-4h4.6a14 14 0 0 1 0 4zm.2 5.6a15.6 15.6 0 0 0 1.4-3.6h3a8 8 0 0 1-4.4 3.6zM16.3 14a16 16 0 0 0 0-4h3.4a8 8 0 0 1 0 4z"/></svg>
        <span>www.brookfernvet.com</span>
      </li>
      <li class="contact-item address">
        <svg class="contact-icon" viewBox="0 0 24 24" aria-hidden="true"><path d="M12 2a7 7 0 0 0-7 7c0 5.2 7 13 7 13s7-7.8 7-13a7 7 0 0 0-7-7zm0 9.5A2.5 2.5 0 1 1 12 6.5a2.5 2.5 0 0 1 0 5z"/></svg>
        <span>14/B, Fernhill Lane<br>Pincode - 560418</span>
      </li>
    </ul>
  </section>

  <section class="card card-back">
    <div class="brand-mark on-white">
      <svg class="ring" width="200" height="200" viewBox="0 0 200 200" aria-hidden="true">
        <circle cx="100" cy="100" r="95" fill="none" stroke="var(--navy)" stroke-width="3"/>
      </svg>
      <span class="brand-name">BROOKFERN</span>
      <span class="brand-sub">VETERINARY HOSPITAL</span>
    </div>
  </section>

</main>
</body>
</html>
```